Looking to design a new sign for our church.

Looking for a new sign
4 x 8 feet dimension
We are renaming the church "Medlow Ridge Community Church"
looking for legible graphics
Would like some type of backdrop being a family tree (oak) / open to other ideas as you are led
I have included a pic of the old sign for your review
would like to incorporate our ministry logo on the lower right hand corner of the sign / see file attached

```html
<!DOCTYPE html>
<html lang="en">
<head>
<meta charset="utf-8">
<title>Medlow Ridge Community Church – Sign</title>
<link rel="stylesheet" href="https://fonts.googleapis.com/css2?family=Jost:ital,wght@1,600&family=Montserrat:wght@500;600&display=swap">
<style>
  :root {
    --navy: #00226b;
    --royal: #0a3fb8;
    --glow: #1a63f5;
    --accent: #1a5ef0;
    --white: #ffffff;
    --shadow: #13285a;
    --faint: rgba(140, 170, 235, 0.55);
  }
  * { margin: 0; padding: 0; box-sizing: border-box; }
  html, body { width: 1200px; height: 692px; overflow: hidden; background: #e6e6e6; }
  .sign {
    position: relative;
    width: 1200px;
    height: 692px;
    overflow: hidden;
    background: radial-gradient(ellipse 430px 420px at 230px 160px, var(--glow) 0%, #1248cf 40%, var(--royal) 62%, var(--navy) 100%);
    background-color: var(--navy);
  }
  .title {
    position: absolute;
    font-family: "Jost", sans-serif;
    font-style: italic;
    font-weight: 600;
    font-size: 182px;
    line-height: 1;
    color: var(--white);
    letter-spacing: -2px;
    text-shadow: 8px 8px 0 var(--shadow);
    white-space: nowrap;
  }
  .title--first { left: 205px; top: 88px; }
  .title--second { left: 452px; top: 248px; }
  .subtitle {
    position: absolute;
    left: 292px;
    width: 662px;
    top: 452px;
    text-align: center;
    font-family: "Montserrat", sans-serif;
    font-weight: 600;
    font-size: 62px;
    color: var(--white);
    white-space: nowrap;
  }
  .divider { position: absolute; left: 311px; top: 543px; }
  .service {
    position: absolute;
    left: 300px;
    width: 650px;
    top: 597px;
    text-align: center;
    font-family: "Montserrat", sans-serif;
    font-weight: 500;
    font-size: 37px;
    letter-spacing: 1px;
    color: var(--white);
  }
  .mark-faint {
    position: absolute;
    left: 44px;
    top: 250px;
    width: 210px;
    text-align: center;
    font-family: "Montserrat", sans-serif;
    font-weight: 600;
    font-size: 30px;
    line-height: 1.2;
    color: var(--faint);
  }
  .mark-faint-circle {
    position: absolute;
    left: 65px; top: 445px;
    width: 168px; height: 168px;
    border-radius: 50%;
    background: var(--faint);
    opacity: 0.55;
  }
  .ministry-top {
    position: absolute;
    left: 948px; top: 70px;
    width: 200px;
    display: flex;
    flex-direction: column;
    align-items: center;
    gap: 14px;
  }
  .ministry-top__circle {
    width: 96px; height: 96px;
    border-radius: 50%;
    background: var(--accent);
  }
  .ministry-top__name {
    font-family: "Montserrat", sans-serif;
    font-weight: 600;
    font-size: 22px;
    line-height: 1.2;
    text-align: center;
    color: var(--white);
  }
  .ministry-arch {
    position: absolute;
    left: 1023px; top: 368px;
    width: 132px; height: 294px;
    border-radius: 66px 66px 0 0;
    background: linear-gradient(180deg, #1a63f5 0%, #0f47cc 60%, #0b3bb4 100%);
    display: flex;
    flex-direction: column;
    align-items: center;
    justify-content: flex-end;
    padding-bottom: 28px;
    gap: 12px;
  }
  .ministry-arch__circle {
    width: 70px; height: 70px;
    border-radius: 50%;
    background: var(--white);
  }
  .ministry-arch__name {
    font-family: "Montserrat", sans-serif;
    font-weight: 600;
    font-size: 15px;
    line-height: 1.25;
    text-align: center;
    color: var(--white);
  }
</style>
</head>
<body>
  <main class="sign">
    <div class="mark-faint">Ridgeway<br>Fellowship</div>
    <div class="mark-faint-circle"></div>

    <div class="title title--first">Medlow</div>
    <div class="title title--second">Ridge</div>

    <div class="ministry-top">
      <div class="ministry-top__circle"></div>
      <div class="ministry-top__name">Hearthside<br>Ministries</div>
    </div>

    <div class="subtitle">Community Church</div>

    <svg class="divider" width="626" height="18" viewBox="0 0 626 18" aria-hidden="true">
      <line x1="0" y1="9" x2="302" y2="9" stroke="#ffffff" stroke-width="1.5"/>
      <line x1="324" y1="9" x2="626" y2="9" stroke="#ffffff" stroke-width="1.5"/>
      <rect x="307" y="3" width="12" height="12" fill="#ffffff" transform="rotate(45 313 9)"/>
    </svg>

    <div class="service">10AM WORSHIP SERVICE</div>

    <div class="ministry-arch">
      <div class="ministry-arch__name">Ridgeway<br>Fellowship</div>
      <div class="ministry-arch__circle"></div>
    </div>
  </main>
</body>
</html>
```